Design a building access mobile app for Tally by Halvorn Portal Systems

Hello, We're looking for an awesome designer to create an app design for our app Tally, by Halvorn Portal Systems. the mobile app allows employees open their office doors with their mobile phone. this means they don't have to use those plastic card badges or keys. We like clean modern design, dark and light themes. We don't have a logo yet.
Updates

Reason: Waiting on a couple designers to submit concepts

Target Market(s)

Commercial and employees

Industry/Entity Type

Building

Font styles to use
Sans Serif
Other font styles liked:
• Oswald extra light

Requirements
Must have
• nice clean design

```html
<!DOCTYPE html>
<html lang="en">
<head>
<meta charset="utf-8">
<title>Tally by Halvorn Portal Systems – Unlock Screen</title>
<link href="https://fonts.googleapis.com/css2?family=Oswald:wght@200;300;400&family=Roboto:wght@400&display=swap" rel="stylesheet">
<style>
  :root {
    --bg-deep: #1c78c4;
    --bg-light: #1fa6d8;
    --screen: #ffffff;
    --ink: #1d1d1f;
    --accent: #3b82cc;
    --accent-light: #6aa6e2;
    --halo: rgba(120, 165, 220, 0.22);
    --door-fill: #f4f5f6;
    --door-line: #dfe1e4;
    --divider: #ececec;
  }
  * { margin: 0; padding: 0; box-sizing: border-box; }
  html, body { width: 1200px; height: 864px; overflow: hidden; }
  body {
    background: linear-gradient(135deg, var(--bg-light) 0%, var(--bg-deep) 100%);
    font-family: "Oswald", sans-serif;
    position: relative;
  }
  .app-screen {
    position: absolute;
    left: 381px; top: 42px;
    width: 438px; height: 780px;
    background: var(--screen);
    box-shadow: 0 20px 50px rgba(10, 50, 90, 0.35);
    overflow: hidden;
  }
  .status-bar {
    height: 24px;
    display: flex; align-items: center; justify-content: space-between;
    padding: 0 8px;
    font-family: "Roboto", sans-serif;
    font-size: 12px; color: var(--ink);
  }
  .status-left, .status-right { display: flex; align-items: center; gap: 4px; width: 130px; }
  .status-right { justify-content: flex-end; }
  .status-time { font-weight: 400; }
  .nav-title {
    height: 40px;
    text-align: center;
    font-weight: 300;
    font-size: 19px;
    letter-spacing: 0.5px;
    line-height: 38px;
    color: var(--ink);
    border-bottom: 1px solid var(--divider);
  }
  .location-button {
    display: block;
    margin: 14px auto 0;
    width: 396px; height: 52px;
    border-radius: 26px;
    background: var(--accent);
    color: #dfeaf7;
    font-family: "Oswald", sans-serif;
    font-weight: 200;
    font-size: 19px;
    letter-spacing: 0.6px;
    border: none;
  }
  .door-illustration {
    position: absolute;
    left: 70px; top: 180px;
    width: 300px; height: 520px;
    background: var(--door-fill);
    border: 1px solid var(--door-line);
  }
  .unlock-control {
    position: absolute;
    left: 129px; top: 330px;
    width: 180px; height: 180px;
    border-radius: 50%;
    background: radial-gradient(circle, var(--halo) 55%, rgba(120,165,220,0.08) 72%, rgba(255,255,255,0) 100%);
    display: flex; align-items: center; justify-content: center;
  }
  .unlock-button {
    width: 130px; height: 130px;
    border-radius: 50%;
    background: linear-gradient(135deg, var(--accent-light), var(--accent));
    display: flex; align-items: center; justify-content: center;
    border: none;
  }
</style>
</head>
<body>
  <main class="app-screen">
    <header class="status-bar">
      <div class="status-left">
        <svg width="30" height="8" viewBox="0 0 30 8" aria-hidden="true">
          <circle cx="3" cy="4" r="2.6" fill="#1d1d1f"/><circle cx="9" cy="4" r="2.6" fill="#1d1d1f"/><circle cx="15" cy="4" r="2.6" fill="#1d1d1f"/>
          <circle cx="21" cy="4" r="2.3" fill="none" stroke="#1d1d1f" stroke-width="0.8"/><circle cx="27" cy="4" r="2.3" fill="none" stroke="#1d1d1f" stroke-width="0.8"/>
        </svg>
        <span>Nimbo</span>
        <svg width="13" height="10" viewBox="0 0 13 10" aria-hidden="true">
          <path d="M6.5 9.5 L0.8 3.2 A8 8 0 0 1 12.2 3.2 Z" fill="#1d1d1f"/>
        </svg>
      </div>
      <span class="status-time">1:23 AM</span>
      <div class="status-right">
        <svg width="7" height="11" viewBox="0 0 7 11" aria-hidden="true">
          <path d="M1 3 L6 8 L3.5 10.5 V0.5 L6 3 L1 8" fill="none" stroke="#1d1d1f" stroke-width="1"/>
        </svg>
        <span>77%</span>
        <svg width="26" height="11" viewBox="0 0 26 11" aria-hidden="true">
          <rect x="0.5" y="0.5" width="22" height="10" rx="2" fill="none" stroke="#1d1d1f"/>
          <rect x="2" y="2" width="15" height="7" fill="#1d1d1f"/>
          <rect x="23.5" y="3.5" width="2" height="4" fill="#1d1d1f"/>
        </svg>
      </div>
    </header>

    <h1 class="nav-title">HALVORN PORTAL SYSTEMS</h1>

    <button class="location-button">OFFICE LOCATION</button>

    <div class="door-illustration" role="img" aria-label="Light pencil sketch of a panelled office door"></div>

    <div class="unlock-control">
      <button class="unlock-button" aria-label="Unlock door">
        <svg width="44" height="44" viewBox="0 0 44 44" aria-hidden="true">
          <path d="M10 20 V13 A8 8 0 0 1 26 13 V15" fill="none" stroke="#fff" stroke-width="3.5" stroke-linecap="round"/>
          <rect x="6" y="20" width="30" height="20" rx="3" fill="#fff"/>
          <circle cx="21" cy="28" r="3" fill="var(--accent)"/>
          <rect x="19.8" y="29" width="2.4" height="6" fill="var(--accent)"/>
        </svg>
      </button>
    </div>
  </main>
</body>
</html>
```